The Morrow Ledgers Website

I need a website to help promote the series of science fiction novels that I am in the process of writing.

I have some content and photos and am in the process of getting some new book cover artwork designed.

I have a current website/domain etc http://www.vantorpagehouse.co.nz but I need something a little more professional and eye catchig but I also want to be able to manage the content myself.

I can send e-versions of the two completed novels for context to any takers

```html
<!DOCTYPE html>
<html lang="en">
<head>
<meta charset="utf-8">
<title>The Morrow Ledgers</title>
<link rel="stylesheet" href="https://fonts.googleapis.com/css2?family=Arimo:wght@400;700&family=Tinos&family=Caveat&display=swap">
<style>
:root{
  --green:#97b92a;
  --green-dark:#7f9e1f;
  --white:#ffffff;
  --panel:#efefef;
  --ink:#333333;
  --muted:#6b6b6b;
  --faint:#9a9a9a;
  --rule:#dcdcdc;
  --accent:#e05a2a;
}
*{box-sizing:border-box;margin:0;padding:0}
html,body{width:1200px;height:1110px;overflow:hidden}
body{background:var(--white);font-family:'Arimo',Arial,sans-serif;color:var(--ink);position:relative}
h1,h2,h3{font-weight:400}
.abs{position:absolute}
.center{left:0;width:1200px;text-align:center}

.topbar{top:0;left:0;width:1200px;height:30px;background:var(--white)}
.nav{left:347px;top:11px;display:flex;gap:20px;font-size:8.5px;color:var(--muted)}
.nav .active{color:var(--green)}
.contact-mail{left:724px;top:12px;font-size:7.5px;color:var(--faint)}
.nav-divider{left:826px;top:6px;width:1px;height:22px;background:var(--rule)}
.social-dot{top:9px;width:14px;height:14px;border-radius:50%;background:#8a8a8a}

.masthead{top:30px;left:0;width:1200px;height:115px;background:var(--green);color:var(--white)}
.series-title{top:30px;font-family:'Tinos',Georgia,serif;font-size:31px}
.author-row{top:73px;left:0;width:1200px;display:flex;justify-content:center;align-items:center;gap:12px}
.author-line{font-size:9px;white-space:nowrap;line-height:11px}
.author-rule{width:92px;height:1px;background:var(--white);margin-top:6px}

.hero{top:145px;left:0;width:1200px;height:225px;background:var(--white)}
.book-art{left:400px;top:30px;width:144px;height:158px}
.tagline{left:575px;top:73px;font-family:'Caveat',cursive;font-size:25px;line-height:28.5px;color:var(--green);white-space:nowrap}

.showcase{top:370px;left:0;width:1200px;height:618px;background:var(--panel);border-top:1px solid #e2e2e2}
.welcome-title{top:26px;font-size:13.5px;color:var(--ink)}
.welcome-sub{top:45px;font-size:9.5px;color:var(--muted)}
.welcome-copy{left:394px;top:76px;width:430px;text-align:center;font-size:7.2px;line-height:10px;color:var(--muted)}
.divider{top:133px;left:347px;width:519px;height:1px;background:var(--rule)}
.read-more{left:581px;top:123px;width:64px;height:20px;background:var(--green);border:1px solid var(--green-dark);color:var(--white);font-size:6.5px;font-weight:700;text-align:center;line-height:18px}

.book-card{top:171px;width:161px;height:170px;background:var(--white)}
.card-cover{left:0;top:0;width:161px;height:108px}
.card-name{top:117px;left:0;width:161px;text-align:center;font-size:7px;line-height:9px;color:var(--ink)}
.card-rule{top:139px;left:12px;width:137px;height:1px;background:var(--rule)}
.card-links{top:147px;left:0;width:161px;text-align:center;font-size:6.3px;color:var(--faint);white-space:nowrap}
.card-links .on{color:var(--green);text-decoration:underline}

.author-box{top:361px;left:347px;width:519px;height:109px;background:var(--white)}
.author-photo{left:49px;top:22px;width:54px;height:64px}
.author-heading{left:128px;top:20px;font-size:9.5px;color:var(--muted)}
.slider-arrows{left:468px;top:18px;font-size:10px;color:#c8c8c8}
.post-meta{left:128px;top:42px;font-size:7px;color:var(--ink);white-space:nowrap}
.post-meta em{color:var(--green);font-size:6.5px}
.post-body{left:128px;top:61px;width:345px;font-size:6.3px;line-height:9px;color:var(--faint)}
.post-body span{color:var(--accent)}

.buy-title{top:497px;font-size:12px;color:var(--muted)}
.buy-list{top:523px;font-size:7px;line-height:12.3px;color:var(--muted)}
.buy-note{top:568px;font-size:7px;line-height:9.5px;color:var(--muted)}

.footer-band{top:988px;left:0;width:1200px;height:91px;background:var(--green);color:var(--white)}
.touch-title{top:23px;font-size:8.5px}
.touch-icons{top:46px;left:561px;display:flex;gap:4px}
.touch-icons i{display:block;width:15px;height:15px;border-radius:50%;background:var(--white)}
.legal{top:1092px;font-size:5.8px;color:var(--ink)}
</style>
</head>
<body>

<header class="abs topbar">
  <nav class="abs nav">
    <span class="active">Home</span><span>Reviews</span><span>About Us</span><span>Blogs</span><span>Contact Us</span><span>Links</span>
  </nav>
  <div class="abs contact-mail">arlen@vantorpagehouse.co.nz</div>
  <div class="abs nav-divider"></div>
  <div class="abs social-dot" style="left:836px"></div>
  <div class="abs social-dot" style="left:853px"></div>
</header>

<section class="abs masthead">
  <h1 class="abs center series-title">The Morrow Ledgers</h1>
  <div class="abs author-row">
    <span class="author-rule"></span>
    <span class="author-line">AUTHOR : ARLEN WHITCOMBE</span>
    <span class="author-rule"></span>
  </div>
</section>

<section class="abs hero">
  <svg class="abs book-art" viewBox="0 0 144 158" role="img" aria-label="Book cover artwork for the second novel, hardcover and small edition">
    <defs>
      <linearGradient id="coverTone" x1="0" y1="0" x2="1" y2="1">
        <stop offset="0" stop-color="#2a2a2a"/><stop offset="0.5" stop-color="#5a4f48"/><stop offset="1" stop-color="#111"/>
      </linearGradient>
    </defs>
    <rect x="0" y="8" width="92" height="150" fill="#cfcfcf"/>
    <rect x="6" y="2" width="88" height="150" fill="url(#coverTone)"/>
    <rect x="92" y="55" width="52" height="103" fill="#cfcfcf"/>
    <rect x="96" y="50" width="46" height="104" fill="url(#coverTone)"/>
  </svg>
  <p class="abs tagline">The Morrow Ledgers arrive on<br>Arlen's scifi page where you will find<br>links to all his scifi novels.</p>
</section>

<main class="abs showcase">
  <h2 class="abs center welcome-title">WELCOME TO MORROW</h2>
  <p class="abs center welcome-sub">The most advanced and commanding civilisation anywhere in the charted galaxy.</p>
  <p class="abs welcome-copy">The Lantern Tide is the second book in the Morrow Ledgers series and picks up after the first book, where two reluctant heroes were seized by a starving survey crew sent out from the Planet Morrow.</p>
  <div class="abs divider"></div>
  <div class="abs read-more">READ MORE</div>

  <article class="abs book-card" style="left:443px">
    <svg class="abs card-cover" viewBox="0 0 161 108" role="img" aria-label="Cover art for The Ember Manifest, a grey moon on black">
      <defs><radialGradient id="moonTone" cx="0.45" cy="0.75" r="0.6"><stop offset="0" stop-color="#b8b8b8"/><stop offset="0.7" stop-color="#6e6e6e"/><stop offset="1" stop-color="#0d0d0d"/></radialGradient></defs>
      <rect width="161" height="108" fill="url(#moonTone)"/>
    </svg>
    <div class="abs card-name">MORROW<br>THE EMBER MANIFEST</div>
    <div class="abs card-rule"></div>
    <div class="abs card-links"><span class="on">Inkleaf Version</span> &nbsp;| &nbsp; Hardcopy Version &nbsp;| &nbsp;Buy Now!</div>
  </article>

  <article class="abs book-card" style="left:623px">
    <svg class="abs card-cover" viewBox="0 0 161 108" role="img" aria-label="Cover art for The Lantern Tide, a ringed planet arc on black">
      <defs><linearGradient id="ringTone" x1="0" y1="1" x2="1" y2="0"><stop offset="0" stop-color="#7a6a5e"/><stop offset="0.45" stop-color="#3a332e"/><stop offset="1" stop-color="#050505"/></linearGradient></defs>
      <rect width="161" height="108" fill="url(#ringTone)"/>
    </svg>
    <div class="abs card-name">MORROW<br>THE LANTERN TIDE</div>
    <div class="abs card-rule"></div>
    <div class="abs card-links">Inkleaf Version &nbsp;| &nbsp; Hardcopy Version &nbsp;| &nbsp;Buy Now!</div>
  </article>

  <section class="abs author-box">
    <svg class="abs author-photo" viewBox="0 0 54 64" role="img" aria-label="Portrait photo of the author">
      <defs><linearGradient id="portraitTone" x1="0" y1="0" x2="0" y2="1"><stop offset="0" stop-color="#6b1f1f"/><stop offset="1" stop-color="#3b6f9a"/></linearGradient></defs>
      <rect width="54" height="64" fill="url(#portraitTone)"/>
    </svg>
    <h3 class="abs author-heading">AUTHOR SAY'S</h3>
    <div class="abs slider-arrows">&lsaquo; &rsaquo;</div>
    <p class="abs post-meta"><em>Friday, 14 March 2014</em> &nbsp;- NZ Harbour Party searches for a clear role in the present day</p>
    <p class="abs post-body">This week Prime Minister Dale Harrow set the date for the coming election. As expected the NZ Harbour Party under Owen Latimer rushed out fighting, sure that they remain the chief opposition voice in New Zealand and hold some sort of natural claim to govern the nation. Brace yourself for a long step backwards should the Harbour Party win <span>[.....]</span></p>
  </section>

  <h2 class="abs center buy-title">Where to BUY the Ember Manifest</h2>
  <p class="abs center buy-list">Inkleaf Version from Riverlane<br>Epub and other versions from Quillmarket<br>Hardcopy Version</p>
  <p class="abs center buy-note">Start reading Morrow - The Ember Manifest (The Morrow Ledgers) on your Inkleaf in under a minute. Don't have an Inkleaf?<br><u>Get your Inkleaf here.</u></p>
</main>

<footer class="abs footer-band">
  <h2 class="abs center touch-title">GET IN TOUCH</h2>
  <div class="abs touch-icons"><i></i><i></i><i></i><i></i><i></i><i></i></div>
</footer>
<p class="abs center legal">THE MORROW LEDGER &nbsp; Privacy Policy &nbsp;| &nbsp;Copyright All Right Reserved 2014.</p>

</body>
</html>
```